corvalistrims.ca vehicle wrap

We need a wrap designed for Kestrel Van used for sales. We import an innovative gutter system from Sweden then market and distribute across Canada. We want to showcase the versatilty, functionality and asthetics of individual components in a technical theme. View files and instructionsh at https://halvornroofline.example.com/:f:/s/extranet/QwPzRt4mxn8LoVTcKe2Dh_PLM7_bzu-kT3rBWjXQ8NpdsR?e=KmWQRT
Target Market(s)
Contractors, Architects and builders.
Industry/Entity Type
Construction Company
Colors
Designer to choose colors to be used in the design.
Look and feel
Each slider illustrates characteristics of the customer's brand and the style your logo design should communicate.

```html
<!DOCTYPE html>
<html lang="en">
<head>
<meta charset="utf-8">
<title>corvalistrims.ca vehicle wrap</title>
<link rel="stylesheet" href="https://fonts.googleapis.com/css2?family=Montserrat:wght@600&family=Oswald:wght@500&display=swap">
<style>
  :root {
    --paper: #ffffff;
    --charcoal: #3a3a3e;
    --charcoal-deep: #2b2b2e;
    --copper: #b8732e;
    --silver: #e6e6e6;
    --ink: #2e2e30;
    --white: #ffffff;
  }
  html, body {
    margin: 0;
    padding: 0;
    width: 1200px;
    height: 792px;
    overflow: hidden;
    background: var(--paper);
  }
  .wrap-canvas {
    position: relative;
    width: 1200px;
    height: 792px;
  }
  .wrap-artwork {
    position: absolute;
    inset: 0;
  }
  .brand-name {
    position: absolute;
    left: 280px;
    top: 345px;
    width: 560px;
    text-align: center;
    font-family: "Montserrat", sans-serif;
    font-weight: 600;
    font-size: 62px;
    line-height: 80px;
    color: var(--white);
    letter-spacing: -1px;
    white-space: nowrap;
    transform: rotate(-10deg);
    transform-origin: center;
  }
  .phone-line {
    position: absolute;
    left: 330px;
    top: 488px;
    width: 600px;
    height: 44px;
    display: flex;
    justify-content: center;
    align-items: center;
    gap: 26px;
    font-family: "Oswald", sans-serif;
    font-weight: 500;
    font-size: 34px;
    color: var(--ink);
    white-space: nowrap;
    transform: rotate(-10.1deg);
    transform-origin: center;
  }
  .phone-number {
    display: flex;
    align-items: center;
    gap: 8px;
  }
  .phone-icon {
    width: 20px;
    height: 20px;
  }
</style>
</head>
<body>
<main class="wrap-canvas">
  <svg class="wrap-artwork" viewBox="0 0 1200 792" width="1200" height="792">
    <defs>
      <linearGradient id="partsTone" x1="0" y1="0" x2="1" y2="1">
        <stop offset="0" stop-color="#e9e9e6"/>
        <stop offset="1" stop-color="#b9b9b5"/>
      </linearGradient>
      <clipPath id="panelClip">
        <rect x="40" y="140" width="1120" height="530" rx="26"/>
      </clipPath>
    </defs>
    <g clip-path="url(#panelClip)">
      <rect class="panel-base" x="40" y="140" width="1120" height="530" fill="var(--charcoal)"/>
      <polygon class="upper-sweep" points="40,140 820,140 40,420" fill="var(--silver)"/>
      <polygon class="upper-accent" points="820,140 870,140 40,444 40,420" fill="var(--copper)"/>
      <polygon class="phone-band" points="40,590 1160,390 1160,440 40,640" fill="var(--silver)"/>
      <polygon class="lower-sweep" points="40,640 1160,440 1160,670 40,670" fill="var(--copper)"/>
      <rect class="rocker-band" x="40" y="602" width="1120" height="26" fill="var(--charcoal-deep)"/>
      <polygon class="rocker-accent" points="40,645 300,628 300,640 40,657" fill="var(--silver)"/>
    </g>
    <rect class="product-visual" x="880" y="250" width="250" height="230" rx="12" fill="url(#partsTone)" role="img" aria-label="Gutter components: outlet, bracket and downpipe branch"/>
  </svg>

  <div class="brand-name">corvalistrims.ca</div>

  <div class="phone-line">
    <span class="phone-number">
      <svg class="phone-icon" viewBox="0 0 20 20"><circle cx="10" cy="10" r="10" fill="var(--copper)"/><path d="M6.5 5.5c.6-.4 1.3 0 1.6.7l.5 1.2c.2.5 0 .9-.4 1.2l-.5.4c.5 1.2 1.4 2.2 2.6 2.8l.4-.5c.3-.4.8-.5 1.2-.3l1.2.6c.6.3.9 1 .5 1.6-.6.9-1.6 1.3-2.6.9-2.6-1-4.5-3-5.4-5.6-.3-1 .1-2.4.9-3z" fill="var(--white)"/></svg>
      1.855.555.0142
    </span>
    <span class="phone-number">
      <svg class="phone-icon" viewBox="0 0 20 20"><circle cx="10" cy="10" r="10" fill="var(--copper)"/><path d="M6.5 5.5c.6-.4 1.3 0 1.6.7l.5 1.2c.2.5 0 .9-.4 1.2l-.5.4c.5 1.2 1.4 2.2 2.6 2.8l.4-.5c.3-.4.8-.5 1.2-.3l1.2.6c.6.3.9 1 .5 1.6-.6.9-1.6 1.3-2.6.9-2.6-1-4.5-3-5.4-5.6-.3-1 .1-2.4.9-3z" fill="var(--white)"/></svg>
      604.555.0187
    </span>
  </div>
</main>
</body>
</html>
```